April 11th Event- Islamorada- Coaching/Tarot/Hypnotherapy

Hi! Need a flyer that can also be posted on social media. Directions attached. Also will need a version that 2 can fit on 1 piece of paper so I can cut in half for hand outs. PDF example attached as well so you can understand. Thank you!

AAAAAAAAAAAAAAAAAAAAAAAAAAAAAAAAAAAAAAAAAAAAAAAAAAAAAAAAAAAAAAAAAAAAAAAAAAAAAAAAAAAAAAAAAAAAAAAAAAAAAAAAAAAAAAAAAAAAAAAAAAAAAAAAAAAAAAAAAAAAAAAAAAAAAAAAAAAAAAAAAAAAAAAAAAAAAAAAAAAAAAAAAAAAAAAAAAAAAAAAAAAAAAAAAAAAAAAAAAAAAAAAAA

Target Market(s)

Female audience age 35-70.
Spiritual, sophisticated

Industry/Entity Type

Event Planning

Font styles to use
Serif

Colors
d2a4cc
3176b5
85acd3
b868aa
e667a6
eea4c8
f59296
fbf289
add136

Requirements
Must have
• See attachments
Nice to have
• See attachments

```html
<!DOCTYPE html>
<html lang="en">
<head>
<meta charset="utf-8">
<title>Get the 411 – Evening Event Flyers</title>
<link href="https://fonts.googleapis.com/css2?family=Marcellus+SC&family=Questrial&family=Lato:ital,wght@0,400;0,700;1,400&display=swap" rel="stylesheet">
<style>
  :root{
    --backdrop:#b5b5b5;
    --paper:#ffffff;
    --ink:#1d1d1d;
    --navy:#03243a;
    --title-blue:#1f5fae;
    --line-blue:#3176b5;
    --soft-blue:#85acd3;
    --label-purple:#b868aa;
    --pink:#e667a6;
    --ticket:#2f5468;
    --teal-a:#eef4f5;
    --teal-b:#7db6c1;
    --alert:#e0201a;
    --serif:"Marcellus SC", Georgia, serif;
    --sans:"Questrial", Arial, sans-serif;
    --body:"Lato", Arial, sans-serif;
  }
  *{margin:0;padding:0;box-sizing:border-box}
  html,body{width:1200px;height:902px;overflow:hidden;background:var(--backdrop)}
  .canvas{position:relative;width:1200px;height:902px;font-family:var(--body);color:var(--ink)}
  p,h1,h2{line-height:1.2}
  .version-label{position:absolute;font-family:var(--body);font-weight:700;font-size:27px;color:#111;transform:translateX(-50%);line-height:1.2}
  .flyer{position:absolute;background:var(--paper);overflow:hidden}
  .abs{position:absolute}
  .center{left:0;right:0;text-align:center}
  .title{font-family:var(--serif);color:#222;line-height:1;font-weight:400}
  .subtitle{font-family:var(--serif);color:var(--title-blue);line-height:1.15}
  .invite{font-family:var(--sans);color:#111;line-height:1.25}
  .detail{font-family:var(--body);font-weight:700;color:#111;line-height:1.2}
  .detail .key{color:var(--label-purple);font-weight:400}
  .detail-note{font-family:var(--body);font-weight:700;color:#111;line-height:1}
  .speakers-label{font-family:var(--body);font-weight:700;color:var(--label-purple);line-height:1}
  .speaker{text-align:center;font-family:var(--body);line-height:1.25;color:#333}
  .speaker .name{font-size:1.5em;line-height:1.2;color:#111}
  .divider{background:#ccc;width:1px}
  .contact-band{background:linear-gradient(90deg,var(--teal-a) 35%,var(--teal-b))}
  .ticket{background:var(--ticket);color:#fff;font-family:var(--body);font-weight:700;text-align:center}
  .glasses{background:#6f8c9b;border-radius:2px}
  .contact-head{font-family:var(--body);color:#222;line-height:1}
  .contact-head b{font-weight:700}
  .contact-line{font-family:var(--body);color:#222;display:flex;align-items:center;gap:4px;line-height:1}
  .sign-off{font-family:var(--body);font-style:italic;color:#333;line-height:1}
  .guest-note{font-family:var(--body);color:var(--alert);line-height:1}
  .rule{height:2px;background:var(--line-blue)}
  .ornament{background:linear-gradient(180deg,#d3e3f3,#9fc0e2);border-radius:40% 40% 6px 6px}
  .ornament.pink{background:linear-gradient(180deg,#f3c3dc,#d88ac0)}
  .photo{background:radial-gradient(ellipse at 40% 45%,rgba(225,210,200,.45),rgba(240,236,232,.25) 55%,rgba(255,255,255,0) 75%)}
</style>
</head>
<body>
<div class="canvas">

  <div class="version-label" style="left:305px;top:70px">Printing</div>
  <div class="version-label" style="left:907px;top:234px">For social media</div>

  <section class="flyer print" style="left:74px;top:121px;width:503px;height:706px">
    <div class="abs photo" role="img" aria-label="Faint photo of a woman with arms outstretched on a beach" style="left:0;top:250px;width:280px;height:430px"></div>

    <h1 class="abs center title" style="top:33px;font-size:33px">Get the 411</h1>
    <p class="abs center subtitle" style="top:64px;font-size:22px">Open Yourself Up To The Info<br>You Have Inside</p>

    <div class="abs navy-band" style="left:0;top:122px;width:503px;height:128px;background:var(--navy)">
      <div class="abs" role="img" aria-label="Pink line mandala ornament" style="left:63px;top:0;width:377px;height:128px;background:radial-gradient(ellipse at 50% 0%,rgba(230,103,166,.75),rgba(230,103,166,.25) 60%,rgba(3,36,58,0) 80%)"></div>
    </div>

    <p class="abs center invite" style="top:264px;font-size:16px">Please Join Us For An Evening of<br>Self Discovery, and Enlightment and Fun!</p>

    <div class="abs ornament" role="img" aria-label="Blue scroll ornament" style="left:170px;top:325px;width:162px;height:38px"></div>
    <div class="abs rule" style="left:72px;top:366px;width:373px"></div>

    <p class="abs center detail" style="top:380px;font-size:13.5px"><span class="key">When:</span> Thursday April 11th</p>
    <p class="abs center detail" style="top:402px;font-size:13.5px"><span class="key">Time:</span> Doors Open at 5:30.&nbsp; Event from 6pm-8pm.</p>
    <p class="abs center detail" style="top:424px;font-size:13.5px"><span class="key">Where:</span> The Gardens at Palm Cove- 40210 Seaside<br>Highway Islamorada</p>
    <p class="abs center detail-note" style="top:459px;font-size:9px">(MM81 Bayside behind Harbor Market)</p>

    <div class="abs rule" style="left:72px;top:473px;width:373px"></div>
    <div class="abs ornament" role="img" aria-label="Blue scroll ornament" style="left:170px;top:477px;width:162px;height:28px;border-radius:6px 6px 40% 40%"></div>

    <p class="abs center speakers-label" style="top:536px;font-size:15px">Speakers:</p>
    <div class="abs speaker" style="left:18px;top:559px;width:170px;font-size:8.5px"><div class="name">Carla Bennet</div>Licensed Hypnotherapist-<br>Serene Path Holistic Therapies</div>
    <div class="abs divider" style="left:186px;top:555px;height:46px"></div>
    <div class="abs speaker" style="left:188px;top:557px;width:152px;font-size:8.5px"><div class="name">Marissa Dale</div>The Bright Spirit Life Coach-<br>Certified Professional Life Coach</div>
    <div class="abs divider" style="left:342px;top:555px;height:46px"></div>
    <div class="abs speaker" style="left:340px;top:557px;width:160px;font-size:8.5px"><div class="name">Joan Sterling</div>Tarot Readings/<br>Inner Way Spiritual Counselor</div>

    <div class="abs contact-band" style="left:33px;top:611px;width:470px;height:72px"></div>
    <div class="abs ticket" style="left:33px;top:611px;width:144px;height:72px">
      <div class="abs glasses" role="img" aria-label="Champagne glasses icon" style="left:7px;top:22px;width:22px;height:32px"></div>
      <div class="abs" style="left:40px;top:5px;width:100px;font-size:17px;line-height:1.2">TICKETS<br>$15 EACH</div>
      <div class="abs" style="left:40px;top:55px;width:100px;font-size:11px;line-height:1">Drinks included</div>
    </div>
    <p class="abs guest-note" style="left:41px;top:686px;font-size:8.5px">Names must be on the guest list</p>
    <p class="abs contact-head" style="left:205px;top:626px;font-size:13px">CONTACT <b>MARISSA DALE</b> FOR TICKETS:</p>
    <p class="abs contact-line" style="left:198px;top:650px;font-size:10px">
      <svg width="9" height="7" viewBox="0 0 9 7"><rect x=".5" y=".5" width="8" height="6" fill="none" stroke="#3176b5"/><path d="M.5 .5 4.5 4 8.5 .5" fill="none" stroke="#3176b5"/></svg>
      marissa@brightspiritcoach.com&nbsp;&nbsp;
      <svg width="9" height="9" viewBox="0 0 10 10"><circle cx="5" cy="5" r="4.5" fill="none" stroke="#3176b5"/><path d="M3.2 2.8c.3 1.8 1.6 3.3 3.5 3.9l.6-.9" fill="none" stroke="#3176b5"/></svg>
      305-555-0142
    </p>
    <p class="abs sign-off" style="left:280px;top:671px;font-size:10px">Hope to see you there!</p>
  </section>

  <section class="flyer social" style="left:617px;top:294px;width:547px;height:385px">
    <div class="abs" style="left:0;top:0;width:209px;height:385px;background:#000">
      <div class="abs" role="img" aria-label="Pink line half mandala ornament" style="left:0;top:0;width:209px;height:385px;background:radial-gradient(ellipse at 0% 50%,rgba(230,103,166,.7),rgba(230,103,166,.25) 60%,rgba(0,0,0,0) 80%)"></div>
    </div>
    <div class="abs photo" role="img" aria-label="Faint photo of a woman with arms outstretched on a beach" style="left:380px;top:20px;width:167px;height:290px"></div>

    <div class="abs" style="left:209px;top:0;width:338px;height:385px">
      <h2 class="abs center title" style="top:26px;font-size:24px">Get the 411</h2>
      <p class="abs center subtitle" style="top:50px;font-size:16.5px">Open Yourself Up To The Info<br>You Have Inside</p>
      <p class="abs center invite" style="top:92px;font-size:11.5px">Please Join Us For An Evening of Self Discovery,<br>and Enlightment and Fun!</p>
      <div class="abs ornament pink" role="img" aria-label="Pink scroll ornament" style="left:123px;top:130px;width:92px;height:18px"></div>
      <div class="abs rule" style="left:55px;top:148px;width:228px;background:var(--label-purple)"></div>
      <p class="abs center detail" style="top:159px;font-size:8.5px"><span class="key">When:</span> Thursday April 11th</p>
      <p class="abs center detail" style="top:174px;font-size:8.5px"><span class="key">Time:</span> Doors Open at 5:30.&nbsp; Event from 6pm-8pm.</p>
      <p class="abs center detail" style="top:188px;font-size:8.5px"><span class="key">Where:</span> The Gardens at Palm Cove- 40210 Seaside<br>Highway Islamorada</p>
      <p class="abs center detail-note" style="top:213px;font-size:6.5px">(MM81 Bayside behind Harbor Market)</p>
      <div class="abs rule" style="left:55px;top:229px;width:228px;background:var(--label-purple)"></div>
      <div class="abs ornament pink" role="img" aria-label="Pink scroll ornament" style="left:123px;top:232px;width:92px;height:18px;border-radius:6px 6px 40% 40%"></div>
      <p class="abs center speakers-label" style="top:267px;font-size:10px">Speakers:</p>
      <div class="abs speaker" style="left:-2px;top:290px;width:120px;font-size:6px"><div class="name">Carla Bennet</div>Licensed Hypnotherapist-<br>Serene Path Holistic Therapies</div>
      <div class="abs speaker" style="left:112px;top:286px;width:110px;font-size:6px"><div class="name">Marissa Dale</div>The Bright Spirit Life Coach-<br>Certified Professional Life Coach</div>
      <div class="abs speaker" style="left:222px;top:290px;width:120px;font-size:6px"><div class="name">Joan Sterling</div>Tarot Readings/<br>Inner Way Spiritual Counselor</div>
    </div>

    <div class="abs contact-band" style="left:215px;top:326px;width:332px;height:49px"></div>
    <div class="abs ticket" style="left:215px;top:326px;width:89px;height:37px">
      <div class="abs glasses" role="img" aria-label="Champagne glasses icon" style="left:5px;top:10px;width:12px;height:20px"></div>
      <div class="abs" style="left:22px;top:3px;width:64px;font-size:10px;line-height:1.2">TICKETS<br>$15 EACH</div>
      <div class="abs" style="left:22px;top:28px;width:64px;font-size:6.5px;line-height:1">Drinks included</div>
    </div>
    <p class="abs guest-note" style="left:219px;top:367px;font-size:6px">Names must be on the guest list</p>
    <p class="abs contact-head" style="left:328px;top:336px;font-size:9px">CONTACT <b>MARISSA DALE</b> FOR TICKETS:</p>
    <p class="abs contact-line" style="left:322px;top:353px;font-size:7px">
      <svg width="7" height="5" viewBox="0 0 9 7"><rect x=".5" y=".5" width="8" height="6" fill="none" stroke="#3176b5"/><path d="M.5 .5 4.5 4 8.5 .5" fill="none" stroke="#3176b5"/></svg>
      marissa@brightspiritcoach.com&nbsp;
      <svg width="7" height="7" viewBox="0 0 10 10"><circle cx="5" cy="5" r="4.5" fill="none" stroke="#3176b5"/><path d="M3.2 2.8c.3 1.8 1.6 3.3 3.5 3.9l.6-.9" fill="none" stroke="#3176b5"/></svg>
      305-555-0142
    </p>
    <p class="abs sign-off" style="left:375px;top:366px;font-size:9px">Hope to see you there!</p>
  </section>

</div>
</body>
</html>
```